Birch Flooring Supply

Basic one-sided business card design using the attached logo. Vintage americana theme. Font is modified Arial Nova Cond, but anything that coordinates can be used

```html
<!DOCTYPE html>
<html lang="en">
<head>
<meta charset="utf-8">
<title>Birch Flooring Supply – Business Card</title>
<link rel="stylesheet" href="https://fonts.googleapis.com/css2?family=Lato:wght@400&family=Roboto+Condensed:wght@700&display=swap">
<style>
  :root {
    --page-bg: #e9e4e0;
    --card-dark: #1c1714;
    --card-mid: #2e2723;
    --bronze: #a27652;
    --bronze-soft: rgba(162, 118, 82, 0.55);
    --text-light: #d2c9c0;
    --text-muted: #bdb2a8;
  }
  * { box-sizing: border-box; margin: 0; padding: 0; }
  html, body { width: 1200px; height: 737px; overflow: hidden; }
  body { background: var(--page-bg); position: relative; }

  .business-card {
    position: absolute;
    left: 60px; top: 66px;
    width: 1080px; height: 604px;
    background: radial-gradient(circle at 30% 50%, var(--card-mid) 0%, var(--card-dark) 70%);
    box-shadow: 0 10px 30px rgba(0,0,0,0.25);
    overflow: hidden;
  }

  .brand-name {
    position: absolute;
    left: 40px; top: 276px;
    width: 564px;
    text-align: center;
    font-family: "Roboto Condensed", sans-serif;
    font-weight: 700;
    font-size: 40px;
    line-height: 48px;
    letter-spacing: 0.5px;
    text-transform: uppercase;
    color: var(--bronze);
    white-space: nowrap;
  }

  .contact-block { position: absolute; left: 571px; top: 128px; }
  .person-name {
    font-family: "Roboto Condensed", sans-serif;
    font-weight: 700;
    font-size: 40px;
    color: var(--bronze);
    letter-spacing: 0.5px;
    line-height: 1;
  }
  .person-title {
    font-family: "Lato", sans-serif;
    font-size: 26px;
    color: var(--text-light);
    margin-top: 10px;
  }
  .title-rule {
    width: 100px; height: 2px;
    background: var(--text-muted);
    margin-top: 14px;
  }
  .contact-list { list-style: none; margin-top: 30px; }
  .contact-item {
    display: flex; align-items: flex-start;
    font-family: "Lato", sans-serif;
    font-size: 24px;
    line-height: 30px;
    color: var(--text-muted);
    margin-bottom: 19px;
  }
  .contact-item.address { margin-bottom: 32px; }
  .contact-icon {
    flex: none;
    width: 34px; height: 34px;
    margin-right: 10px;
    border-radius: 3px;
    background: var(--bronze-soft);
    display: flex; align-items: center; justify-content: center;
  }
  .contact-icon svg { width: 22px; height: 22px; fill: var(--card-dark); }
</style>
</head>
<body>
  <main class="business-card">
    <p class="brand-name">Birch Flooring Supply</p>

    <section class="contact-block">
      <h1 class="person-name">DANIEL R. HARTWELL</h1>
      <p class="person-title">Managing Director</p>
      <div class="title-rule"></div>
      <ul class="contact-list">
        <li class="contact-item address">
          <span class="contact-icon"><svg viewBox="0 0 24 24"><path d="M12 2a7 7 0 0 0-7 7c0 5 7 13 7 13s7-8 7-13a7 7 0 0 0-7-7zm0 9.5A2.5 2.5 0 1 1 12 6.5a2.5 2.5 0 0 1 0 5z"/></svg></span>
          <span>1275 Linden Avenue<br>Springfield, IL 62704</span>
        </li>
        <li class="contact-item">
          <span class="contact-icon"><svg viewBox="0 0 24 24"><path d="M6.6 10.8a15 15 0 0 0 6.6 6.6l2.2-2.2c.3-.3.7-.4 1-.2 1.1.4 2.3.6 3.6.6.6 0 1 .4 1 1V20c0 .6-.4 1-1 1A17 17 0 0 1 3 4c0-.6.4-1 1-1h3.5c.6 0 1 .4 1 1 0 1.3.2 2.5.6 3.6.1.3 0 .7-.2 1z"/></svg></span>
          <span>+00 555 019 24</span>
        </li>
        <li class="contact-item">
          <span class="contact-icon"><svg viewBox="0 0 24 24"><path d="M3 5h18v14H3zm2 2v.5l7 5 7-5V7zm0 3v7h14v-7l-7 5z"/></svg></span>
          <span>office@birchflooringsupply.com</span>
        </li>
        <li class="contact-item">
          <span class="contact-icon"><svg viewBox="0 0 24 24"><path d="M6 3l12 9-5.5 1 3 6.5-2.2 1-3-6.5L6 18z"/></svg></span>
          <span>www.birchflooringsupply.com</span>
        </li>
      </ul>
    </section>
  </main>
</body>
</html>
```